buseisness card

design a card that similar to my web site
TRELLINGWORKSLLC .COM

Contact Information for Business Card

NAME PHONE # WEBSITE EMAIL AND DISCTIPTION OF WHAT WE DO

Colors
0054AA
0677BA
7BADD7
CADEEF
E8F1F8

Requirements
Must have
• lOGO AND DETAILS
Nice to have
• I LIKE THE WATER LIKE ON MY WEB SITE

```html
<!DOCTYPE html>
<html lang="en">
<head>
<meta charset="utf-8">
<title>Trelling Works – Business Card</title>
<link rel="stylesheet" href="https://fonts.googleapis.com/css2?family=Montserrat:wght@400;500;700&display=swap">
<style>
  :root {
    --page-bg: #dfe6ea;
    --navy: #0c2f4e;
    --brand-blue: #1f6ea8;
    --logo-blue: #3a83bd;
    --card-white: #eef0f2;
    --text-blue: #1d5e93;
    --water-light: #2a9bc4;
    --water-mid: #136a97;
    --water-deep: #0b3a5c;
    --white: #ffffff;
  }
  * { box-sizing: border-box; margin: 0; padding: 0; }
  html, body { width: 1200px; height: 1000px; overflow: hidden; }
  body {
    background: var(--page-bg);
    font-family: "Montserrat", sans-serif;
    position: relative;
  }
  .card {
    position: absolute;
    left: 250px;
    width: 700px;
    height: 400px;
    border-radius: 56px;
    overflow: hidden;
    box-shadow: 0 18px 40px rgba(12, 47, 78, 0.25);
  }
  .card--front { top: 70px; background: var(--card-white); }
  .card--back { top: 530px; }

  .front-shape { position: absolute; inset: 0; width: 100%; height: 100%; }

  .brand {
    position: absolute;
    display: flex;
    flex-direction: column;
    align-items: center;
    gap: 12px;
  }
  .brand__dot { border-radius: 50%; }
  .brand__name { font-weight: 700; letter-spacing: 1px; white-space: nowrap; }

  .card--front .brand { left: 30px; top: 140px; width: 250px; }
  .card--front .brand__dot { width: 54px; height: 54px; background: var(--logo-blue); }
  .card--front .brand__name { color: var(--logo-blue); font-size: 21px; }

  .details {
    position: absolute;
    left: 385px;
    top: 78px;
    color: var(--text-blue);
  }
  .details__company { font-size: 26px; font-weight: 700; letter-spacing: 0.5px; }
  .details__role { font-size: 15px; font-weight: 500; margin-bottom: 18px; }
  .contact-list { list-style: none; display: flex; flex-direction: column; gap: 10px; }
  .contact-list li { display: flex; align-items: flex-start; gap: 12px; font-size: 15px; line-height: 1.2; }
  .contact-list svg { width: 14px; height: 14px; flex: none; margin-top: 2px; fill: var(--text-blue); }

  .water {
    position: absolute;
    inset: 0;
    background:
      radial-gradient(ellipse at 50% 110%, var(--water-deep) 0%, transparent 60%),
      linear-gradient(170deg, var(--water-deep) 0%, var(--water-light) 38%, var(--water-mid) 62%, var(--water-deep) 100%);
  }
  .card--back .brand { left: 0; right: 0; top: 130px; }
  .card--back .brand__dot { width: 70px; height: 70px; background: var(--white); }
  .card--back .brand__name { color: var(--white); font-size: 30px; }
</style>
</head>
<body>
  <section class="card card--front" aria-label="Business card front">
    <svg class="front-shape" viewBox="0 0 700 400" preserveAspectRatio="none" aria-hidden="true">
      <path d="M0 0 H318 C262 110 400 250 336 400 H0 Z" fill="var(--brand-blue)"/>
      <path d="M0 0 H300 C244 110 382 250 318 400 H0 Z" fill="var(--navy)"/>
    </svg>
    <div class="brand">
      <span class="brand__dot"></span>
      <span class="brand__name">TRELLING WORKS</span>
    </div>
    <div class="details">
      <h1 class="details__company">TRELLING WORKS</h1>
      <p class="details__role">CEO</p>
      <ul class="contact-list">
        <li><svg viewBox="0 0 24 24"><path d="M6.6 10.8a15.1 15.1 0 0 0 6.6 6.6l2.2-2.2a1 1 0 0 1 1-.25 11.4 11.4 0 0 0 3.6.57 1 1 0 0 1 1 1V20a1 1 0 0 1-1 1A17 17 0 0 1 3 4a1 1 0 0 1 1-1h3.5a1 1 0 0 1 1 1c0 1.25.2 2.45.57 3.57a1 1 0 0 1-.25 1z"/></svg>+740 555 0148</li>
        <li><svg viewBox="0 0 24 24"><path d="M2 5h20v14H2z M2 5l10 8 10-8" fill="none" stroke="var(--text-blue)" stroke-width="2.4"/></svg>jd@tw247.com</li>
        <li><svg viewBox="0 0 24 24"><circle cx="12" cy="12" r="9.5" fill="none" stroke="var(--text-blue)" stroke-width="2"/><path d="M2.5 12h19M12 2.5c3 3 3 16 0 19M12 2.5c-3 3-3 16 0 19" fill="none" stroke="var(--text-blue)" stroke-width="1.6"/></svg>trellingworksllc.com</li>
        <li><svg viewBox="0 0 24 24"><path d="M12 2a7 7 0 0 0-7 7c0 5 7 13 7 13s7-8 7-13a7 7 0 0 0-7-7zm0 9.5A2.5 2.5 0 1 1 12 6.5a2.5 2.5 0 0 1 0 5z"/></svg><span>1840 Harbor Point<br>Drive<br>Riverton, OH 43100</span></li>
      </ul>
    </div>
  </section>

  <section class="card card--back" aria-label="Business card back">
    <div class="water" role="img" aria-label="Underwater photograph of the sea surface with light rays"></div>
    <div class="brand">
      <span class="brand__dot"></span>
      <span class="brand__name">TRELLING WORKS</span>
    </div>
  </section>
</body>
</html>
```